Print materials for 3-star hotel

We are changing up our print materials (notepads, letterheads, key card jackets, small flyer for the room rates) We are a 3 star business hotel in the Philippines and have mainly used grey tones and clean, simple lines. See attached photos for logo and hotel interior photos.

Target Market(s)

Business

Contact Information for Business Card

Tamarind Crest Hotel
Governor Lualhati Avenue corner Pindang St Cebu City 6000 Philippines
Tel: +63 32 480 5273
Mobile: +63 917 608 4926
www.tamarindcresthotel.example

Font styles to use
Serif
Sans Serif

Requirements
Must have
• Simple
• Readable font and font size
Nice to have
• Neutral colors, grey and taupes
Should not have
• No purples and bright blues

```html
<!DOCTYPE html>
<html lang="en">
<head>
<meta charset="utf-8">
<title>Tamarind Crest Hotel – Print Suite</title>
<link href="https://fonts.googleapis.com/css2?family=Tinos:wght@400;700&family=Lato:wght@400;700&display=swap" rel="stylesheet">
<style>
:root{
  --board:#bbbcbe;
  --paper:#ffffff;
  --ink:#1a1a1a;
  --night:#151515;
  --brown:#5a3221;
  --brown-dark:#4a2716;
  --body:#6b6b6b;
  --muted:#8a8a8a;
  --shadow:0 4px 6px rgba(0,0,0,.18);
}
*{margin:0;padding:0;box-sizing:border-box}
html,body{width:1200px;height:1200px;overflow:hidden;background:var(--board)}
body{position:relative;font-family:'Lato',sans-serif;color:var(--ink)}
.piece{position:absolute;box-shadow:var(--shadow)}
.wordmark{font-family:'Tinos',serif;font-weight:400;text-transform:uppercase;text-align:center;line-height:1.25}
.wordmark .sub{display:block}
.photo{position:absolute}

/* flyer */
.flyer{left:142px;top:114px;width:376px;height:532px;background:var(--paper)}
.flyer .wordmark{position:absolute;top:27px;left:0;width:100%;font-size:12px;letter-spacing:3px}
.flyer .wordmark .sub{font-size:8px;letter-spacing:3px}
.photo-main{left:0;top:75px;width:270px;height:311px;background:linear-gradient(160deg,#3a2116 0%,#5e3a26 35%,#d8d2c8 55%,#2a1a12 75%,#c78a2c 100%)}
.photo-side{left:275px;width:99px;height:99px}
.photo-pool{top:78px;background:linear-gradient(180deg,#a9c6dc,#c9ccc8 60%,#5aa7b8)}
.photo-lobby{top:182px;background:linear-gradient(160deg,#e0b25a,#7a4a24 55%,#3a2216)}
.photo-hall{top:284px;background:linear-gradient(170deg,#f1eee9,#d8c7a8 60%,#b9b3ab)}
.price{position:absolute;left:32px;top:362px;width:170px;height:43px;border-radius:22px;background:var(--brown);border:2px solid #fff;box-shadow:0 0 0 1px var(--brown);color:#fff;font-family:'Tinos',serif;font-size:31px;line-height:39px;text-align:center}
.room-title{position:absolute;left:39px;top:418px;font-family:'Tinos',serif;font-weight:400;font-size:14px;color:var(--brown-dark)}
.room-desc{position:absolute;left:40px;top:446px;width:200px;font-size:5.6px;line-height:1.35;color:#444}
.includes{position:absolute;left:287px;top:420px}
.includes h3{font-family:'Tinos',serif;font-weight:400;font-size:13px;color:#222}
.includes ul{margin:6px 0 0 6px;font-size:6px;line-height:1.5;color:#444}
.flyer-foot{position:absolute;left:0;top:486px;width:100%;height:46px;background:var(--brown);color:#fff;font-size:5.2px}
.flyer-foot .col{position:absolute;top:9px;line-height:11px}
.flyer-foot .col-phones{left:36px}
.flyer-foot .col-online{left:122px}
.flyer-foot .col-address{left:262px;width:106px}
.ci{display:flex;align-items:center;gap:5px;white-space:nowrap}
.ci svg{width:6px;height:6px;flex:none}
.indent{padding-left:11px;white-space:nowrap}

/* letterhead */
.letter{left:547px;top:114px;width:378px;height:532px;background:var(--paper)}
.letter .wordmark{position:absolute;top:72px;left:0;width:100%;font-size:9px;letter-spacing:2px}
.letter .wordmark .sub{font-size:6px;letter-spacing:3px}
.salute{position:absolute;left:43px;top:131px;font-size:5.6px;color:#333}
.letter-body{position:absolute;left:43px;top:162px;width:291px;font-family:'Tinos',serif;font-size:5.5px;line-height:1.38;color:var(--body);text-align:justify}
.letter-body p{margin-bottom:8px}
.letter-body .lead{font-family:'Lato',sans-serif;font-weight:700;color:#333}
.signature{position:absolute;left:43px;top:350px;width:56px;height:16px;background:linear-gradient(90deg,#eee,#ddd)}
.letter-contact{position:absolute;left:43px;top:428px;font-size:4.3px;line-height:8.4px;color:#555}

/* business cards */
.card{width:202px;height:115px}
.card-back{left:909px;top:254px;background:var(--night);display:flex;align-items:center;justify-content:center}
.card-back .wordmark{color:#fff;font-size:10px;letter-spacing:2px}
.card-front{left:912px;top:397px;width:201px;height:114px;background:var(--paper)}
.card-front .wordmark{position:absolute;left:14px;top:40px;width:82px;font-size:6px;letter-spacing:1px}
.card-front .wordmark .sub{font-size:4.4px;letter-spacing:2px}
.holder{position:absolute;left:14px;top:70px;width:82px;text-align:center;font-family:'Tinos',serif;font-size:6px;line-height:1.2;color:#333}
.holder small{display:block;font-size:5px;color:var(--brown)}
.card-contact{position:absolute;left:108px;top:29px;font-size:3.6px;line-height:7.9px;color:#555}
.card-contact .ci{gap:4px}
.card-contact .ci svg{width:4px;height:4px}
.card-contact .indent{padding-left:8px}

/* notepad */
.notepad{left:283px;top:717px;width:275px;height:376px;background:var(--night)}
.notepad .holes{position:absolute;left:16px;top:10px}
.notepad .wordmark{position:absolute;left:0;top:190px;width:100%;color:#fff;font-size:14px;letter-spacing:3px}
.notepad .wordmark .sub{font-size:10px;letter-spacing:5px}
.notepad .web{position:absolute;bottom:10px;width:100%;text-align:center;font-family:'Tinos',serif;font-size:4.5px;color:#aaa;letter-spacing:.5px}

/* key card jackets */
.jacket{top:800px;width:144px;height:202px;background:var(--night);overflow:hidden}
.jacket .notch{position:absolute;left:44px;top:-28px;width:56px;height:56px;border-radius:50%;background:var(--brown)}
.jacket-front{left:598px}
.jacket-back{left:762px}
.welcome{position:absolute;top:57px;width:100%;text-align:center;font-family:'Tinos',serif;font-size:7px;letter-spacing:9px;color:#fff}
.jacket-front .wordmark{position:absolute;top:117px;width:100%;color:#fff;font-size:8px;letter-spacing:2px}
.jacket-front .wordmark .sub{font-size:6px;letter-spacing:3px}
.room-line{position:absolute;left:22px;top:167px;width:102px;font-size:3.5px;color:#ccc;border-bottom:.5px solid #555;padding-bottom:1px}
.jacket-back .wordmark{position:absolute;top:82px;width:100%;color:#fff;font-size:13px;letter-spacing:2px}
.jacket-back .wordmark .sub{font-size:9px;letter-spacing:4px}
</style>
</head>
<body>

<svg width="0" height="0" style="position:absolute">
  <defs>
    <symbol id="ico-phone" viewBox="0 0 10 10"><path d="M2 0.5 L3.8 2.6 L2.8 3.7 Q4 6 6.3 7.2 L7.4 6.2 L9.5 8 L8.2 9.5 Q3.5 9 0.5 1.8 Z" fill="currentColor"/></symbol>
    <symbol id="ico-fax" viewBox="0 0 10 10"><rect x="2.5" y="0.5" width="5" height="3" fill="currentColor"/><rect x="0.5" y="3.5" width="9" height="4.5" rx="1" fill="currentColor"/><rect x="2.5" y="7" width="5" height="2.5" fill="currentColor"/></symbol>
    <symbol id="ico-mail" viewBox="0 0 10 10"><rect x="0.5" y="2" width="9" height="6" fill="currentColor"/><path d="M0.5 2 L5 5.5 L9.5 2" stroke="#fff" stroke-width=".8" fill="none"/></symbol>
    <symbol id="ico-web" viewBox="0 0 10 10"><circle cx="5" cy="5" r="4.2" fill="none" stroke="currentColor" stroke-width="1.1"/><path d="M0.8 5 H9.2 M5 0.8 V9.2" stroke="currentColor" stroke-width=".8"/></symbol>
    <symbol id="ico-pin" viewBox="0 0 10 10"><path d="M5 0.5 A3.3 3.3 0 0 1 8.3 3.8 C8.3 6 5 9.5 5 9.5 C5 9.5 1.7 6 1.7 3.8 A3.3 3.3 0 0 1 5 0.5 Z" fill="currentColor"/><circle cx="5" cy="3.8" r="1.2" fill="#fff"/></symbol>
  </defs>
</svg>

<!-- Room rate flyer -->
<section class="piece flyer">
  <div class="wordmark">Tamarind Crest<span class="sub">Hotel</span></div>
  <div class="photo photo-main" role="img" aria-label="Photo of a superior guest room with a white double bed, lamp and brown sofa"></div>
  <div class="photo photo-side photo-pool" role="img" aria-label="Photo of the hotel building and outdoor pool"></div>
  <div class="photo photo-side photo-lobby" role="img" aria-label="Photo of the warmly lit restaurant"></div>
  <div class="photo photo-side photo-hall" role="img" aria-label="Photo of the bright lobby and reception"></div>
  <div class="price">P2,850.00</div>
  <h2 class="room-title">Superior &amp; Delux Rooms</h2>
  <p class="room-desc">This room has two (2) Single Beds and can accommodate one &amp; two persons, and an additional extra person. Extra person charge...</p>
  <div class="includes">
    <h3>Includes:</h3>
    <ul><li>GYM</li><li>SAUNA</li><li>POOL</li></ul>
  </div>
  <footer class="flyer-foot">
    <div class="col col-phones">
      <div class="ci"><svg><use href="#ico-phone"/></svg>+63 32 480 5273</div>
      <div class="ci"><svg><use href="#ico-phone"/></svg>+63 917 608 4926</div>
      <div class="ci"><svg><use href="#ico-phone"/></svg>+63 918 240 7719</div>
    </div>
    <div class="col col-online">
      <div class="ci"><svg><use href="#ico-fax"/></svg>+63 32 480 5290</div>
      <div class="ci"><svg><use href="#ico-mail"/></svg>reservations@tamarindcresthotel.example</div>
      <div class="ci"><svg><use href="#ico-web"/></svg>www.tamarindcresthotel.example</div>
    </div>
    <div class="col col-address">
      <div class="ci"><svg><use href="#ico-pin"/></svg>Governor Lualhati Avenue corner</div>
      <div class="indent">Pindang St, Cebu City, Cebu, 6000,</div>
      <div class="indent">Philippines</div>
    </div>
  </footer>
</section>

<!-- Letterhead -->
<section class="piece letter">
  <div class="wordmark">Tamarind Crest<span class="sub">Hotel</span></div>
  <p class="salute">Dear, Mr__________</p>
  <div class="letter-body">
    <p>Lorem Ipsum is simply dummy text of the printing and typesetting industry. Lorem Ipsum has been the industry's standard dummy text ever since the 1500s, when an unknown printer took a galley of type and scrambled it to make a type specimen book. It has survived not only five centuries, but also the leap into electronic typesetting, remaining essentially unchanged. It was popularised in the 1960s with the release of Letraset sheets containing Lorem Ipsum passages, and more recently with desktop publishing software like Aldus PageMaker including versions of Lorem Ipsum.</p>
    <p>Lorem Ipsum is simply dummy text of the printing and typesetting industry. Lorem Ipsum has been the industry's standard dummy text ever since the 1500s, when an unknown printer took a galley of type and scrambled it to make a type specimen book. It has survived not only five centuries, but also the leap into electronic typesetting, remaining essentially unchanged. It was popularised in the 1960s with the release of Letraset sheets containing Lorem Ipsum passages, and more recently with desktop publishing software like Aldus PageMaker including versions of Lorem Ipsum.</p>
    <p class="lead">Lorem Ipsum is simply dummy text of the printing and typesetting industry. Lorem Ipsum has been the industry's standard dummy text ever since the 1500s, when an unknown printer took a galley of type and scrambled it to make a type specimen book.</p>
    <p>Lorem Ipsum is simply dummy text of the printing and typesetting industry. Lorem Ipsum has been the industry's standard dummy text ever since the 1500s, when an unknown printer took a galley of type and scrambled it to make a type specimen book.</p>
  </div>
  <div class="signature" role="img" aria-label="Handwritten signature"></div>
  <div class="letter-contact">
    <div class="ci"><svg><use href="#ico-phone"/></svg>+63 32 480 5273</div>
    <div class="ci"><svg><use href="#ico-phone"/></svg>+63 917 608 4926</div>
    <div class="ci"><svg><use href="#ico-phone"/></svg>+63 918 240 7719</div>
    <div class="ci"><svg style="color:var(--brown)"><use href="#ico-fax"/></svg>+63 32 480 5290</div>
    <div class="ci"><svg style="color:var(--brown)"><use href="#ico-mail"/></svg>reservations@tamarindcresthotel.example</div>
    <div class="ci"><svg style="color:var(--brown)"><use href="#ico-web"/></svg>www.tamarindcresthotel.example</div>
    <div class="ci"><svg style="color:var(--brown)"><use href="#ico-pin"/></svg>Governor Lualhati Avenue corner Pindang St, Cebu City, Cebu, 6000, Philippines</div>
  </div>
</section>

<!-- Business card back -->
<section class="piece card card-back">
  <div class="wordmark">Tamarind Crest</div>
</section>

<!-- Business card front -->
<section class="piece card card-front">
  <div class="wordmark">Tamarind Crest<span class="sub">Hotel</span></div>
  <div class="holder">Marco Dela Vega<small>Agent</small></div>
  <div class="card-contact">
    <div class="ci"><svg><use href="#ico-phone"/></svg>+63 32 480 5273</div>
    <div class="ci"><svg><use href="#ico-phone"/></svg>+63 917 608 4926</div>
    <div class="ci"><svg><use href="#ico-phone"/></svg>+63 918 240 7719</div>
    <div class="ci"><svg><use href="#ico-fax"/></svg>+63 32 480 5290</div>
    <div class="ci"><svg style="color:var(--brown)"><use href="#ico-mail"/></svg>reservations@tamarindcresthotel.example</div>
    <div class="ci"><svg style="color:var(--brown)"><use href="#ico-web"/></svg>www.tamarindcresthotel.example</div>
    <div class="ci"><svg><use href="#ico-pin"/></svg>Governor Lualhati Ave corner Pindang</div>
    <div class="indent">St, Cebu City, Cebu, 6000, Philippines</div>
  </div>
</section>

<!-- Notepad -->
<section class="piece notepad">
  <svg class="holes" width="244" height="10" viewBox="0 0 244 10">
    <g fill="#d6d6d6">
      <circle cx="5" cy="5" r="4.6"/><circle cx="18" cy="5" r="4.6"/><circle cx="31" cy="5" r="4.6"/><circle cx="44" cy="5" r="4.6"/><circle cx="57" cy="5" r="4.6"/><circle cx="70" cy="5" r="4.6"/><circle cx="83" cy="5" r="4.6"/><circle cx="96" cy="5" r="4.6"/><circle cx="109" cy="5" r="4.6"/><circle cx="122" cy="5" r="4.6"/><circle cx="135" cy="5" r="4.6"/><circle cx="148" cy="5" r="4.6"/><circle cx="161" cy="5" r="4.6"/><circle cx="174" cy="5" r="4.6"/><circle cx="187" cy="5" r="4.6"/><circle cx="200" cy="5" r="4.6"/><circle cx="213" cy="5" r="4.6"/><circle cx="226" cy="5" r="4.6"/><circle cx="239" cy="5" r="4.6"/>
    </g>
  </svg>
  <div class="wordmark">Tamarind Crest<span class="sub">Hotel</span></div>
  <div class="web">www.tamarindcresthotel.example</div>
</section>

<!-- Key card jacket, front -->
<section class="piece jacket jacket-front">
  <div class="notch"></div>
  <div class="welcome">WELCOME</div>
  <div class="wordmark">Tamarind Crest<span class="sub">Hotel</span></div>
  <div class="room-line">Room #</div>
</section>

<!-- Key card jacket, back -->
<section class="piece jacket jacket-back">
  <div class="notch"></div>
  <div class="wordmark">Tamarind<br>Crest<span class="sub">Hotel</span></div>
</section>

</body>
</html>
```